依頼詳細
ラベルデザインの制作
今後様々なフレーバーを展開する予定ですので、応用ができるデザインで
お願い致します。
記載項目
サイズ100(タテ)×70(ヨコ)m/m (±10m/mはOKです)
記載項目:品名「ぽりぽりチップ」、「国産米100%使用」、
あと、いいイメージのコピーがあれば入れたいと思います。
形状は四角、楕円、変形(特にこだわりはありません)
希望イメージ
シンプル 複雑
単色 カラフル
暗い 明るい
日常 高級
遊び心 厳粛
未来的 伝統的
女性的 男性的
希望する色
赤系、黄・オレンジ系、緑系
納品ファイル
• 高解像度JPG (.jpg)
• イラストレーター形式 (.ai)
補足説明
■ 選んだ理由

商品特徴にぴったりで、文字とイラストのかわいさ、色合いや形状などとても良かったと思います。

■ 提案者全員のお礼・コメント

この度ワークルの皆様から多くのご提案を頂き感謝申し上げます。
貴重なお時間を掛けて制作して頂いたデザインですが、
ひとつしか選ぶことが出来ないことを申し訳なく思います。
改めてご提案を頂き有り難う御座いました。
また、ご依頼させて頂く機会があると思います。
その時は是非よろしくお願い致します。

```html
<!DOCTYPE html>
<html lang="ja">
<head>
<meta charset="UTF-8">
<title>ぽりぽりチップ ラベル</title>
<link rel="stylesheet" href="https://fonts.googleapis.com/css2?family=Zen+Maru+Gothic:wght@500;700;900&display=swap">
<style>
  :root {
    --pink-light: #f7e1df;
    --pink-mid: #eec5c2;
    --brand-red: #c8463e;
    --copy-red: #c0413a;
    --white: #ffffff;
  }
  html, body {
    margin: 0;
    padding: 0;
    width: 841px;
    height: 1200px;
    overflow: hidden;
    background: var(--pink-light);
  }
  .label {
    position: relative;
    width: 841px;
    height: 1200px;
    overflow: hidden;
    font-family: "Zen Maru Gothic", sans-serif;
  }
  .rice-texture {
    position: absolute;
    inset: 0;
    background: linear-gradient(160deg, var(--pink-mid) 0%, var(--pink-light) 55%, var(--pink-mid) 100%);
  }
  .title-band {
    position: absolute;
    left: 306px;
    top: 0;
    width: 346px;
    height: 1200px;
    background: var(--brand-red);
  }
  .title-band::after {
    content: "";
    position: absolute;
    inset: -4px 12px 14px 12px;
    border: 3px solid var(--white);
    border-radius: 6px;
  }
  .product-name {
    position: absolute;
    left: 50%;
    top: 70px;
    transform: translateX(-50%);
    margin: 0;
    writing-mode: vertical-rl;
    font-weight: 900;
    font-size: 152px;
    line-height: 1;
    letter-spacing: 0.02em;
    color: var(--white);
  }
  .catch-copy {
    position: absolute;
    left: 660px;
    top: 120px;
    margin: 0;
    writing-mode: vertical-rl;
    font-weight: 700;
    font-size: 58px;
    line-height: 1;
    letter-spacing: 0.04em;
    color: var(--copy-red);
  }
  .origin-claim {
    position: absolute;
    left: 200px;
    top: 110px;
    margin: 0;
    writing-mode: vertical-rl;
    text-orientation: upright;
    font-weight: 500;
    font-size: 56px;
    line-height: 1;
    letter-spacing: 0.02em;
    color: var(--copy-red);
  }
  .flavor-badge {
    position: absolute;
    left: -100px;
    top: 830px;
    width: 420px;
    height: 420px;
    border-radius: 50%;
    background: var(--brand-red);
  }
  .flavor-badge::after {
    content: "";
    position: absolute;
    inset: 14px;
    border: 3px solid var(--white);
    border-radius: 50%;
  }
  .flavor-name {
    position: absolute;
    left: 58px;
    top: 920px;
    margin: 0;
    writing-mode: vertical-rl;
    font-weight: 700;
    font-size: 66px;
    line-height: 1;
    letter-spacing: 0.06em;
    color: var(--white);
  }
</style>
</head>
<body>
  <main class="label">
    <div class="rice-texture" role="img" aria-label="淡いピンク地に散らばる米粒模様"></div>

    <p class="origin-claim">国産米100%使用</p>

    <div class="title-band">
      <h1 class="product-name">ぽりぽりチップ</h1>
    </div>

    <p class="catch-copy">お米の風味とサクサク食感。</p>

    <div class="flavor-badge"></div>
    <p class="flavor-name">えび塩</p>
  </main>
</body>
</html>
```